Local Flower Farm Needs Business Card Design

I need business cards designed for a flower farm based in Eudora, Kansas.
Business Info:
We are a local cut flower farm located in Eudora, Kansas, founded by Darla Hoffstrom. What started as a passion for agriculture and search for more joy in daily life has blossomed into a small business dedicated to providing the community with beautiful, fresh, and sustainable flowers. We specialize in local, seasonal blooms, ensuring that every petal reflects the care and dedication we pour into our craft. Our mission is to deliver the highest quality flowers directly to our customers through local farmers markets and to florists who share our commitment to sustainability. Join us in celebrating the beauty of nature, one bloom at a time!
Contact Details:
Darla Hoffstrom
Owner
Phone 913-555-0147
Facebook: Lorabelle Quinn Blossoms
Instagram: @LorabelleQuinnBlossoms
Website: LorabelleQuinnBlossoms.example
Target Market(s)
Wholesale to Florists and Direct to Consumer via Farmers Market
Industry/Entity Type
Florist, Farm
Contact Information for Business Card
Name, Contact Info, Logo
Look and feel

```html
<!DOCTYPE html>
<html lang="en">
<head>
<meta charset="utf-8">
<title>Lorabelle Quinn Blossoms – Business Card</title>
<link rel="stylesheet" href="https://fonts.googleapis.com/css2?family=Montserrat:wght@300;400;700&display=swap">
<style>
  :root {
    --backdrop: #ececec;
    --card-white: #ffffff;
    --forest: #0b2a2e;
    --forest-deep: #0a262a;
    --emboss: #1f5158;
    --ink: #111111;
  }
  * { margin: 0; padding: 0; box-sizing: border-box; }
  html, body { width: 1200px; height: 1108px; overflow: hidden; }
  body {
    background: var(--backdrop);
    font-family: "Montserrat", sans-serif;
    position: relative;
  }
  .card { position: absolute; left: 219px; width: 776px; }
  .card-front { top: 50px; height: 473px; background: var(--card-white); }
  .card-back { top: 568px; height: 456px; background: var(--forest-deep); }

  .header-band {
    position: absolute; left: 0; right: 0; top: 39px; height: 86px;
    background: var(--forest);
  }
  .badge {
    position: absolute; left: 81px; top: 15px; width: 124px; height: 124px;
    border-radius: 50%; background: var(--card-white);
    border: 2px solid var(--forest);
    display: flex; align-items: center; justify-content: center; text-align: center;
    color: var(--forest); font-weight: 700; font-size: 13px; line-height: 1.25;
    letter-spacing: 0.5px; text-transform: uppercase;
  }
  .person {
    position: absolute; right: 50px; top: 51px; text-align: right; color: var(--card-white);
  }
  .person-name { font-weight: 700; font-size: 29px; line-height: 1.1; letter-spacing: 0.2px; }
  .person-role { font-weight: 300; font-size: 18px; margin-top: 3px; }

  .contact-list {
    position: absolute; left: 39px; top: 332px; list-style: none;
    color: var(--ink); font-size: 18px; font-weight: 400;
  }
  .contact-list li { display: flex; align-items: center; height: 28.5px; }
  .contact-icon { width: 17px; height: 17px; margin-right: 9px; flex: none; }

  .brand-mark {
    position: absolute; left: 500px; top: 215px; width: 230px;
    color: var(--forest); font-weight: 700; font-size: 40px; line-height: 1.1;
    text-align: center;
  }

  .back-seal {
    position: absolute; left: 216px; top: 64px; width: 344px; height: 344px;
    border-radius: 50%; border: 2px solid var(--emboss);
    display: flex; align-items: center; justify-content: center; text-align: center;
    color: var(--emboss); font-weight: 700; font-size: 36px; line-height: 1.15;
  }
</style>
</head>
<body>
  <section class="card card-front">
    <div class="header-band"></div>
    <div class="badge">Lorabelle<br>Quinn<br>Blossoms</div>
    <div class="person">
      <div class="person-name">Darla Hoffstrom</div>
      <div class="person-role">Owner</div>
    </div>

    <ul class="contact-list">
      <li>
        <svg class="contact-icon" viewBox="0 0 24 24" aria-hidden="true">
          <path fill="#111" d="M6.6 10.8a15.1 15.1 0 0 0 6.6 6.6l2.2-2.2a1 1 0 0 1 1-.25 11.4 11.4 0 0 0 3.6.57 1 1 0 0 1 1 1V20a1 1 0 0 1-1 1A17 17 0 0 1 3 4a1 1 0 0 1 1-1h3.5a1 1 0 0 1 1 1c0 1.25.2 2.45.57 3.57a1 1 0 0 1-.25 1z"/>
        </svg>913-555-0147
      </li>
      <li>
        <svg class="contact-icon" viewBox="0 0 24 24" aria-hidden="true"><circle cx="12" cy="12" r="10" fill="#111"/></svg>Lorabelle Quinn Blossoms
      </li>
      <li>
        <svg class="contact-icon" viewBox="0 0 24 24" aria-hidden="true"><circle cx="12" cy="12" r="10" fill="#111"/></svg>@LorabelleQuinnBlossoms
      </li>
      <li>
        <svg class="contact-icon" viewBox="0 0 24 24" aria-hidden="true">
          <circle cx="12" cy="12" r="10" fill="none" stroke="#111" stroke-width="2"/>
          <ellipse cx="12" cy="12" rx="4.5" ry="10" fill="none" stroke="#111" stroke-width="1.6"/>
          <path d="M2 12h20" stroke="#111" stroke-width="1.6"/>
        </svg>www.LorabelleQuinnBlossoms.example
      </li>
    </ul>

    <div class="brand-mark">Lorabelle<br>Quinn<br>Blossoms</div>
  </section>

  <section class="card card-back">
    <div class="back-seal">Lorabelle<br>Quinn<br>Blossoms</div>
  </section>
</body>
</html>
```